Dunrest Timesheet App

I need a simple app for Iphone so that my employees can send me the details of where they worked and how many hours they worked for. I have a logo that will need to be integrated into it.
We will need it to also email the information to a centralized address so that the invoicing and wages can be done.
It will need to have the
Date
Mine Worked (This will have a drop down menu with 7 mines listed)
Hours Worked
Vent Report Number
Emergency Response Report Number
Surname
First Name

Target Market(s)

This app if for employees of the company, all fields will need to be filled out, but they can have either a vent report number(V/R) or and Emergency Response Report number (ERC)

Requirements
Must have

• Date
Hours Worked
Vent Report Number
Surname
First Name
Nice to have
• Ability to have app send data in email format or even to have it put into a database at a central location?

```html
<!DOCTYPE html>
<html lang="en">
<head>
<meta charset="utf-8">
<title>Dunrest Timesheet</title>
<link rel="stylesheet" href="https://fonts.googleapis.com/css2?family=Arimo:wght@400;700&family=Open+Sans:wght@400&display=swap">
<style>
  :root {
    --backdrop: #3d3d3d;
    --header-top: #4a4a4a;
    --header-bottom: #2b2b2b;
    --orange-light: #f8961f;
    --orange-deep: #f47a12;
    --field-top: #ffffff;
    --field-bottom: #ececec;
    --field-text: #333333;
    --label: #ffffff;
    --accent: #f07a1a;
    --go-top: #52b947;
    --go-bottom: #1d8a31;
    --white: #ffffff;
  }
  * { margin: 0; padding: 0; box-sizing: border-box; }
  html, body {
    width: 1200px; height: 2241px; overflow: hidden;
    background: var(--backdrop);
  }
  .app-screen {
    position: absolute; left: 0; top: 222px;
    width: 1200px; height: 1796px;
    background: linear-gradient(160deg, var(--orange-light), var(--orange-deep));
    overflow: hidden;
  }
  .app-header {
    position: absolute; left: 0; top: 0; width: 1200px; height: 179px;
    background: linear-gradient(var(--header-top), var(--header-bottom));
    display: flex; align-items: center; justify-content: center; gap: 22px;
  }
  .brand-dot {
    width: 100px; height: 100px; border-radius: 50%;
    background: var(--accent);
  }
  .brand-name {
    font-family: "Arimo", Arial, sans-serif; font-weight: 700;
    font-size: 60px; color: var(--white);
  }
  .field-label {
    position: absolute; left: 244px;
    font-family: "Arimo", Arial, sans-serif; font-size: 49px;
    color: var(--label); line-height: 1;
    text-shadow: 0 2px 3px rgba(0,0,0,.25);
  }
  .field {
    position: absolute; left: 211px; width: 774px; height: 117px;
    border-radius: 13px;
    background: linear-gradient(var(--field-top), var(--field-bottom));
    box-shadow: 0 3px 6px rgba(0,0,0,.18);
    display: flex; align-items: center; justify-content: space-between;
    padding: 0 36px;
    font-family: "Open Sans", Arial, sans-serif; font-size: 42px;
    color: var(--field-text);
  }
  .field svg { flex: none; }
  .send-button {
    position: absolute; left: 211px; top: 1590px; width: 774px; height: 127px;
    border-radius: 10px;
    background: linear-gradient(var(--go-top), var(--go-bottom));
    box-shadow: 0 3px 6px rgba(0,0,0,.2);
    display: flex; align-items: center; justify-content: center;
    font-family: "Arimo", Arial, sans-serif; font-size: 64px; color: var(--white);
  }
</style>
</head>
<body>
<main class="app-screen">
  <header class="app-header">
    <span class="brand-dot"></span>
    <span class="brand-name">Dunrest pty ltd</span>
  </header>

  <span class="field-label" style="top:246px">Surname:</span>
  <div class="field" style="top:299px">jmarlow.works</div>

  <span class="field-label" style="top:431px">Firstname:</span>
  <div class="field" style="top:484px">jmarlow.works</div>

  <span class="field-label" style="top:617px">Date:</span>
  <div class="field" style="top:670px">
    <span>10 - 08 - 2012</span>
    <svg width="62" height="62" viewBox="0 0 24 24" aria-hidden="true">
      <rect x="2.5" y="4" width="19" height="17" rx="2.5" fill="none" stroke="var(--accent)" stroke-width="2"/>
      <rect x="2.5" y="4" width="19" height="4.5" fill="var(--accent)"/>
      <rect x="6.5" y="1.5" width="2" height="4" rx="1" fill="var(--accent)"/>
      <rect x="15.5" y="1.5" width="2" height="4" rx="1" fill="var(--accent)"/>
      <g fill="var(--accent)">
        <rect x="6" y="11" width="2.5" height="2"/><rect x="10.75" y="11" width="2.5" height="2"/><rect x="15.5" y="11" width="2.5" height="2"/>
        <rect x="6" y="15.5" width="2.5" height="2"/><rect x="10.75" y="15.5" width="2.5" height="2"/><rect x="15.5" y="15.5" width="2.5" height="2"/>
      </g>
    </svg>
  </div>

  <span class="field-label" style="top:799px">Mine worked:</span>
  <div class="field" style="top:852px">
    <span>Steel Fixing</span>
    <svg width="50" height="50" viewBox="0 0 24 24" aria-hidden="true">
      <path d="M5 9 L12 16 L19 9" fill="none" stroke="var(--accent)" stroke-width="3" stroke-linecap="round" stroke-linejoin="round"/>
    </svg>
  </div>

  <span class="field-label" style="top:975px">Hours worked:</span>
  <div class="field" style="top:1028px">10</div>

  <span class="field-label" style="top:1150px">V/R:</span>
  <div class="field" style="top:1203px">N/L</div>

  <span class="field-label" style="top:1326px">ERC:</span>
  <div class="field" style="top:1379px">N/L</div>

  <div class="send-button">Send it to email</div>
</main>
</body>
</html>
```